Tolvane Logo & Packaging Design

I need a logo and packaging label for a roll-on deodorant. I have a design in mind, however it needs to be changed to suit the information based in the design brief.

The logo and product label should be a point of differentiation, to help the brand stand out from the masses.

I have attached a detailed brief with all required information, so please review carefully.

Target Market(s)

Modern man working professional, 24-35, $70K+ income, stays fit and healthy

Industry/Entity Type

Hair And Beauty

Requirements
Must have
• colour, bold typeface, logo and graphic.
• please see this landing page for idea reference: http://www.quillhollowtaps.com/our-ales/
• https://cdn1.pixelharbor.net/static/71cd9a22f3c14b0e93a27d58/t/6b293f5635b705217c4e1bc9/1622645315366/KRT
• https://cdn1.pixelharbor.net/static/71cd9a22f3c14b0e93a27d58/t/606808d47b5a74ed79d3e40a/1509023834683/?format=750w
Should not have
• no black and white only.

```html
<!DOCTYPE html>
<html lang="en">
<head>
<meta charset="utf-8">
<title>Tolvane Roll-On Deodorant Label</title>
<link rel="stylesheet" href="https://fonts.googleapis.com/css2?family=Michroma&family=Oswald:wght@600&family=Open+Sans:wght@400&display=swap">
<style>
  :root {
    --backdrop: #f4f4f7;
    --ink: #2f2f2f;
    --silver-edge: #b9b9bb;
    --silver-mid: #f3f3f4;
    --gold-edge: #d8a914;
    --gold-mid: #f4d24a;
  }
  * { margin: 0; padding: 0; box-sizing: border-box; }
  html, body {
    width: 976px;
    height: 1200px;
    overflow: hidden;
    background: var(--backdrop);
  }
  .canvas {
    position: relative;
    width: 976px;
    height: 1200px;
  }
  .label {
    position: absolute;
    left: 138px;
    top: 50px;
    width: 700px;
    height: 1100px;
    overflow: hidden;
  }
  .band {
    position: absolute;
    left: 0;
    width: 100%;
  }
  .band--silver {
    background: linear-gradient(90deg, var(--silver-edge) 0%, var(--silver-mid) 45%, var(--silver-mid) 60%, var(--silver-edge) 100%);
  }
  .band--gold {
    background: linear-gradient(90deg, var(--gold-edge) 0%, var(--gold-mid) 50%, var(--gold-edge) 100%);
  }
  .band--cap { top: 0; height: 34px; }
  .band--top-stripe { top: 34px; height: 17px; }
  .band--upper { top: 51px; height: 506px; }
  .band--lower { top: 557px; height: 423px; }
  .band--bottom-stripe { top: 980px; height: 25px; }
  .band--foot { top: 1005px; height: 95px; }

  .brand {
    position: absolute;
    left: 0;
    top: 360px;
    width: 100%;
    display: flex;
    align-items: center;
    justify-content: center;
    gap: 30px;
  }
  .brand__mark {
    width: 34px;
    height: 34px;
    background: var(--ink);
  }
  .brand__name {
    font-family: "Michroma", sans-serif;
    font-size: 58px;
    letter-spacing: 0.3em;
    color: var(--ink);
    line-height: 1;
  }
  .product-type {
    position: absolute;
    left: 0;
    top: 745px;
    width: 100%;
    text-align: center;
    font-family: "Oswald", sans-serif;
    font-weight: 600;
    font-size: 46px;
    letter-spacing: 0.09em;
    color: var(--ink);
  }
  .audience {
    position: absolute;
    left: 0;
    top: 835px;
    width: 100%;
    text-align: center;
    font-family: "Michroma", sans-serif;
    font-size: 30px;
    letter-spacing: 0.3em;
    color: var(--ink);
  }
  .net-content {
    position: absolute;
    left: 0;
    top: 1030px;
    width: 100%;
    text-align: center;
    font-family: "Open Sans", sans-serif;
    font-size: 33px;
    color: var(--ink);
  }
</style>
</head>
<body>
<main class="canvas">
  <section class="label" aria-label="Tolvane deodorant label">
    <div class="band band--silver band--cap"></div>
    <div class="band band--gold band--top-stripe"></div>
    <div class="band band--silver band--upper"></div>
    <div class="band band--gold band--lower"></div>
    <div class="band band--silver band--bottom-stripe"></div>
    <div class="band band--gold band--foot"></div>

    <div class="brand">
      <span class="brand__mark"></span>
      <span class="brand__name">TOLVANE</span>
    </div>

    <p class="product-type">DEODORANT SPAY</p>
    <p class="audience">MEN</p>
    <p class="net-content">150 ml ℮ 104.5 G 3.6oz</p>
  </section>
</main>
</body>
</html>
```